Stationery Design + Business Cards

Stationary (letterhead as A4 210x297mm and Letter 8.5"x11", preferably both master page + 2nd pages)

Also need business cards, standard size 50x88mm, can be vertical or horizontal.

You can use a front/back design for the business cards, or front only.

Looking at the uploaded file (dolvek, you already have that), I want it to use the first logo on the list (4 colors).

Alternative, try the grayscale version (second file).

I need the following information on the business card (in no particular order, let me know what you come up with): 

Firstname Lastlame 
Title 

Mobile +1 317-555-0147 

Velmarix, Inc. 
24819 Birchwood Ridge Pass 
Carmel, IN 46195 
Tel. +1 317-555-0182 
Fax +1 317-555-0163 

Web: www.velmarix.com 
Twitter: twitter/Velmarix or @Velmarix 
Facebook: pagehub.com/Velmarix 

For letterhead, just the company name, address + phone number & fax number 

If you think the phone/fax or something else should not be on the business cards, or something could be missing, let me know.

```html
<!DOCTYPE html>
<html lang="en">
<head>
<meta charset="utf-8">
<title>Velmarix, Inc. – Business Card Back</title>
<link rel="stylesheet" href="https://fonts.googleapis.com/css2?family=Nunito+Sans:wght@800&family=Quicksand:wght@400;500&display=swap">
<style>
  :root {
    --ink: #000000;
    --paper: #ffffff;
  }
  html, body {
    margin: 0;
    padding: 0;
    width: 1200px;
    height: 683px;
    overflow: hidden;
    background: var(--paper);
  }
  .card {
    position: relative;
    width: 1200px;
    height: 683px;
    background: var(--paper);
    overflow: hidden;
  }
  .company-details {
    position: absolute;
    left: 62px;
    top: 60px;
    margin: 0;
    font-family: "Nunito Sans", Arial, sans-serif;
    font-weight: 800;
    font-size: 30px;
    line-height: 40.5px;
    color: var(--ink);
    font-style: normal;
    letter-spacing: -0.2px;
  }
  .company-details span {
    display: block;
  }
  .channel-arc {
    position: absolute;
    inset: 0;
  }
  .channel-label {
    font-family: "Quicksand", Arial, sans-serif;
    font-weight: 500;
    font-size: 30px;
    fill: var(--ink);
  }
  .web-badge-text {
    font-family: "Quicksand", Arial, sans-serif;
    font-weight: 500;
    font-size: 21px;
    fill: var(--paper);
    letter-spacing: 1px;
  }
</style>
</head>
<body>
  <main class="card">
    <address class="company-details">
      <span class="company-name">Velmarix, Inc.</span>
      <span class="street">24819 Birchwood Ridge Pass</span>
      <span class="city">Carmel, IN 46195</span>
      <span class="phone">Tel. +1 317-555-0182</span>
      <span class="fax">Fax +1 317-555-0163</span>
    </address>

    <svg class="channel-arc" width="1200" height="683" viewBox="0 0 1200 683" aria-label="Online channels">
      <path class="arc-line" d="M652 690 C 740 540, 930 400, 1200 378" fill="none" stroke="var(--ink)" stroke-width="3.5"/>

      <circle class="badge badge-profile" cx="697" cy="612" r="50" fill="var(--ink)"/>
      <circle class="badge badge-handle" cx="847" cy="480" r="50" fill="var(--ink)"/>
      <circle class="badge badge-web" cx="1088" cy="395" r="50" fill="var(--ink)"/>
      <text class="web-badge-text" x="1088" y="402" text-anchor="middle">www</text>

      <text class="channel-label" x="1048" y="343" text-anchor="end">www.velmarix.com</text>
      <text class="channel-label" x="804" y="433" text-anchor="end">@Velmarix</text>
      <text class="channel-label" x="648" y="565" text-anchor="end">pagehub.com/Velmarix</text>
    </svg>
  </main>
</body>
</html>
```